DL Flyer Lantern Creek Hotel Thursday Night Bonus

We require a DL Portrait and landscape flyer for our Thursday Night Bonus Pull.
The way the draw works you must be part of our loyalty program, and on a Thursday night anytime between 5pm and 7pm, a name/number will be picked at random. If that person is in the hotel at the time they will win the jackpot.

The jackpot starts at $250 and goes up by $50 each week, if not won.

The things that the flyer must state:-
* loyalty program members only
* drawn on a Thursday night anytime between 5pm and 7pm
* QMRV/58/46271 must be written somewhere.
* see staff for details.
* our logo

Would like the flyer to be catch peoples attention but remain professional

If your unable to download logo, please forward email address and I will send it throuh

```html
<!DOCTYPE html>
<html lang="en">
<head>
<meta charset="utf-8">
<title>Thursday Night Bonus Pull – Lantern Creek Hotel</title>
<link rel="stylesheet" href="https://fonts.googleapis.com/css2?family=UnifrakturCook:wght@700&family=Oswald:wght@500;700&family=Open+Sans:wght@400&display=swap">
<style>
  :root {
    --wood-dark: #141414;
    --wood-mid: #2a2a2a;
    --gold: #d9a441;
    --gold-light: #f3cf6a;
    --gold-deep: #a8741f;
    --gold-muted: #b98a34;
    --canvas-light: #5e5039;
    --canvas-dark: #1c1610;
    --ink: #0f0b07;
  }
  * { margin: 0; padding: 0; box-sizing: border-box; }
  html, body { width: 1200px; height: 638px; overflow: hidden; background: var(--wood-dark); }

  .flyer {
    position: relative;
    width: 1200px;
    height: 638px;
    background: linear-gradient(90deg, var(--wood-dark), var(--wood-mid) 50%, var(--wood-dark));
    overflow: hidden;
  }
  .ticket-frame { position: absolute; inset: 0; }

  .title {
    position: absolute;
    left: 0; right: 0; top: 108px;
    text-align: center;
    font-family: "UnifrakturCook", serif;
    font-weight: 700;
    font-size: 60px;
    letter-spacing: 2px;
    color: var(--gold);
    background: linear-gradient(180deg, var(--gold-light), var(--gold) 55%, var(--gold-deep));
    -webkit-background-clip: text;
    background-clip: text;
    -webkit-text-fill-color: transparent;
    filter: drop-shadow(2px 3px 1px rgba(0,0,0,.8));
  }

  .seal-art {
    position: absolute;
    left: 105px; top: 265px;
    width: 210px; height: 210px;
    border-radius: 50%;
    background: radial-gradient(circle, rgba(185,138,52,.45), rgba(185,138,52,.15) 70%);
  }
  .dice-art {
    position: absolute;
    left: 140px; top: 430px;
    width: 150px; height: 100px;
    border-radius: 10px;
    background: linear-gradient(135deg, #e7b24e, #9c6a1e);
  }

  .members-stamp {
    position: absolute;
    left: 428px; top: 240px;
    width: 470px; height: 160px;
    transform: rotate(-5deg);
    border: 6px solid var(--gold-muted);
    outline: 3px solid var(--gold-muted);
    outline-offset: 8px;
    display: flex; flex-direction: column; justify-content: center; align-items: center;
    font-family: "Oswald", sans-serif;
    font-weight: 700;
    font-size: 48px;
    line-height: 1.05;
    letter-spacing: 3px;
    color: var(--gold-muted);
    text-transform: uppercase;
  }

  .draw-times {
    position: absolute;
    left: 960px; top: 256px;
    width: 110px;
    text-align: center;
    font-family: "Oswald", sans-serif;
    font-weight: 700;
    font-size: 40px;
    line-height: 1;
    color: var(--gold);
    text-shadow: 2px 2px 2px rgba(0,0,0,.7);
  }
  .draw-times .amp { font-size: 26px; display: block; }

  .jackpot-start {
    position: absolute;
    left: 508px; top: 438px;
    width: 92px; height: 92px;
    border: 4px solid var(--gold-muted);
    border-radius: 50%;
    display: flex; align-items: center; justify-content: center;
    transform: rotate(-12deg);
    font-family: "Oswald", sans-serif;
    font-weight: 700;
    font-size: 30px;
    color: var(--gold-muted);
  }
  .jackpot-start sup { font-size: 18px; }

  .fine-print {
    position: absolute;
    left: 318px; top: 512px;
    font-family: "Open Sans", sans-serif;
    font-size: 12.5px;
    line-height: 1.35;
    color: var(--gold);
  }
  .fine-print .permit { display: block; padding-left: 8px; font-size: 11px; }

  .hotel-name {
    position: absolute;
    left: 700px; top: 486px;
    display: flex; align-items: center; gap: 14px;
    font-family: "Oswald", sans-serif;
    font-weight: 500;
    font-size: 34px;
    letter-spacing: 1px;
    color: var(--gold-light);
    text-transform: uppercase;
  }
  .hotel-name .mark { width: 40px; height: 40px; background: var(--gold-light); }
</style>
</head>
<body>
<main class="flyer">
  <svg class="ticket-frame" width="1200" height="638" viewBox="0 0 1200 638" aria-hidden="true">
    <defs>
      <linearGradient id="goldEdge" x1="0" y1="0" x2="1" y2="1">
        <stop offset="0" stop-color="#f3cf6a"/>
        <stop offset=".5" stop-color="#c8912f"/>
        <stop offset="1" stop-color="#f0c860"/>
      </linearGradient>
      <radialGradient id="canvasTone" cx=".5" cy=".4" r=".75">
        <stop offset="0" stop-color="#5e5039"/>
        <stop offset=".7" stop-color="#3a2f22"/>
        <stop offset="1" stop-color="#1c1610"/>
      </radialGradient>
    </defs>
    <rect x="36" y="56" width="1128" height="542" fill="url(#goldEdge)"/>
    <rect x="46" y="66" width="1108" height="522" fill="url(#canvasTone)"/>
    <path d="M100 84 H1100 A38 38 0 0 0 1138 122 V532 A38 38 0 0 0 1100 570 H100 A38 38 0 0 0 62 532 V122 A38 38 0 0 0 100 84 Z"
          fill="none" stroke="#c8912f" stroke-width="6"/>
    <!-- suit corners -->
    <path d="M72 80 L84 96 L72 112 L60 96 Z" fill="#c8912f"/>
    <g fill="#c8912f">
      <circle cx="1128" cy="84" r="7"/><circle cx="1120" cy="96" r="7"/><circle cx="1136" cy="96" r="7"/>
      <path d="M1125 96 L1131 96 L1134 110 L1122 110 Z"/>
    </g>
    <path d="M72 578 C58 564 58 550 66 548 C70 547 72 551 72 553 C72 551 74 547 78 548 C86 550 86 564 72 578 Z"
          fill="#c8912f" transform="translate(0 -6) scale(1)"/>
    <g fill="#c8912f">
      <path d="M1128 546 C1142 560 1144 570 1136 572 C1132 573 1129 570 1128 568 C1127 570 1124 573 1120 572 C1112 570 1114 560 1128 546 Z"/>
      <path d="M1125 568 L1131 568 L1134 580 L1122 580 Z"/>
    </g>
  </svg>

  <h1 class="title">Thursday Night Bonus Pull</h1>

  <div class="seal-art" role="img" aria-label="Faded gold bonus stamp seal with dollar sign"></div>
  <div class="dice-art" role="img" aria-label="Two gold dice"></div>

  <div class="members-stamp"><span>Loyalty Program</span><span>Members Only</span></div>

  <p class="draw-times">5PM<span class="amp">&amp;</span>7PM</p>

  <div class="jackpot-start"><span><sup>$</sup>250</span></div>

  <p class="fine-print">* see staff for details.<span class="permit">QMRV/58/46271</span></p>

  <div class="hotel-name"><span class="mark"></span>Lantern Creek Hotel</div>
</main>
</body>
</html>
```